Design for landing page for startup within book publishing and book sales connected to NFT

This is a website design job, not a web development job.
Specification in words
A one page landingpage to market a NFT project. This is a marketing page that has the purpose of building a community and attracting investors. This job is ONLY design in Figma for landing page.

It is for a NFT based project but the idea concerns publishing of books, selling of books and games around books.

The name is pagevance.

Check the site sonwick.io, it is going to be a bit of that concept. Sonwick is music but this is going to be free reading of books.

A simple (clean minimalistic design) is preferable.

The design specification below gives you an idea of how we want that to look.

Also in complement with the design spec then if possible throw in a bit of gaming feeling and also a bit of metaverse feeling.

Give a feeling that attracts authors (not too "NFT like") but still get some feeling of NFT innovation and a bit metaverse.

Mobile responsive.

Parts of page
Menulevel: Logo, Connection to Chirpnet, Harmlink, Quillpost, Wirecast. Join Waitlist.

Banner explaining the concept.

Banner to join waitlist with button.

Part with description of features including some "screenshots" of browsing books (like browsing movies in FLX prime).

Team.

Roadmap.

FAQ.

White paper.

Specification in design

Minimalistic, modern looking. Gradient and shadings if possible. Basically some kind of version of FLX prime is what I see before my eyes. Try to combine Bazarro with FLX prime. FLX prime is a movie site but the design is superior to Bazarro.

For colors, use the color scale of the Zodiac sign Leo. This is an example: https://starcharts.example-zodiaq.com/sign-traits/leo-colors-palettes-help-you-shine

https://www.skyomenhub.co/love/leo-Leo-Color-Characteristics-and-Love-19.html

Gold and purple should be the dominant colors:
https://www.celestiqa.com/zodiac-signs/leo

The colors like this but less aggressive:
​​https://markvesper.movie/

Try to make a good UX/UI design also so that the users easy can interact with the interface.
Updates

Scope of project changed from 5 to 1 page.

As an answer to a question I got: This project is for design only. Nothing else.

Promonged on the request of designers.

Target Market(s)

Book publishing and book purchasing. NFT.

Industry/Entity Type

Book publishing. Book purchase. NFT.

Number of Pages Required

1 page

Font styles to use
Sans Serif

Colors
FFF300
FFF600
FEFA6F
FFFEC7
FFFEE8
FFC000
F8CF3A
FAE287
FDF2CF
FEFAEE
F0912C
F2A743
F7CA91
FBE8D2
FDF5EE
EE7325
F08F49
F5BC92
FAE3D3
FDF4ED
EB3D1F
EC4F4E
F09395
F8D3D4
FCEDEE
E54698
E96AAD
F1A4CE
F9D9EA
FCEFF6
A7469A
B969AE
D3A5CF
EDDBEB
F8F0F9
6B429C
8869AF
B7A5CE
E3DAEB
F3F0F8

Requirements
Must have
• A design that astonishes the users :-).
Nice to have
• Some innovative design.

```html
<!DOCTYPE html>
<html lang="en">
<head>
<meta charset="utf-8">
<title>pagevance — Free reading of books</title>
<link rel="stylesheet" href="https://fonts.googleapis.com/css2?family=Poppins:wght@400;500;600;700&family=Raleway:wght@400;500&display=swap">
<style>
:root{
  --purple-deep:#2a0a9e;
  --purple:#5b10e0;
  --violet:#7a1cf0;
  --orange:#f08f49;
  --orange-deep:#e8613c;
  --coral:#e2574c;
  --peach:#fbe3d3;
  --peach-light:#fdf4ed;
  --yellow:#fff300;
  --ink:#111111;
  --muted:#555555;
  --white:#ffffff;
  --line:#e9e9ee;
}
*{box-sizing:border-box;margin:0;padding:0}
html,body{width:1200px;height:4539px;overflow:hidden}
body{position:relative;background:var(--white);font-family:"Raleway",sans-serif;color:var(--ink)}
.abs{position:absolute}
.pill-btn{position:absolute;display:flex;align-items:center;justify-content:center;border-radius:40px;font-family:"Poppins",sans-serif;font-weight:600;font-size:14px;text-transform:uppercase;z-index:3}

/* header */
.brand{position:absolute;z-index:3;left:88px;top:22px;display:flex;align-items:center;gap:10px;font-family:"Poppins",sans-serif;font-weight:600;font-size:32px;color:var(--white)}
.brand-dot{width:44px;height:44px;border-radius:50%;background:var(--orange)}
.socials{position:absolute;z-index:3;top:28px;right:278px;display:flex;gap:8px}
.social{height:38px;padding:0 12px;border:2px solid var(--white);border-radius:20px;display:flex;align-items:center;font-family:"Poppins",sans-serif;font-size:12px;font-weight:500;color:var(--white)}
.header-cta{left:975px;top:25px;width:135px;height:42px;border:2px solid var(--white);color:var(--white);font-size:12px}

/* hero */
.hero-title{position:absolute;z-index:3;left:85px;top:282px;font-family:"Poppins",sans-serif;font-weight:700;font-size:76px;line-height:72px;color:var(--white);white-space:nowrap}
.hero-title .accent{color:var(--yellow)}
.hero-cta{left:85px;top:525px;width:186px;height:45px;background:var(--orange);color:var(--white);font-size:14px}
.frame{position:absolute;z-index:2;background:var(--white);border-radius:10px;box-shadow:0 14px 40px rgba(30,10,90,.25)}
.cover{position:absolute;border-radius:3px}
.bar{position:absolute;height:8px;border-radius:4px;background:#e3e3ea}

/* browsing */
.section-title{position:absolute;z-index:2;left:0;width:1200px;text-align:center;font-family:"Poppins",sans-serif;font-weight:600;font-size:44px}
.book-card{position:absolute;width:180px;text-align:center}
.book-card .cover{position:relative;width:123px;height:182px;margin:0 auto;box-shadow:6px 8px 16px rgba(0,0,0,.18)}
.book-card h3{margin-top:26px;font-family:"Poppins",sans-serif;font-weight:600;font-size:17px}
.book-card p{margin-top:2px;font-size:13px;line-height:18px;color:var(--muted)}

/* team */
.subtitle{position:absolute;left:0;width:1200px;text-align:center;font-size:15px;color:var(--muted)}
.member{position:absolute;width:240px;text-align:center}
.member .photo{width:211px;height:211px;border-radius:50%;margin:0 auto}
.member h3{margin-top:26px;font-family:"Poppins",sans-serif;font-weight:600;font-size:20px}
.member p{font-size:13px;color:var(--muted)}

/* roadmap */
.road-label{position:absolute;z-index:2;font-family:"Poppins",sans-serif;font-weight:500;font-size:21px;color:var(--ink)}
.road-label.left{text-align:right;width:300px}
.road-icon{position:absolute;z-index:3;width:78px;height:78px;border-radius:50%;background:var(--white);box-shadow:0 6px 18px rgba(0,0,0,.12);display:flex;align-items:center;justify-content:center}
.road-core{position:absolute;z-index:2;left:409px;top:2132px;width:380px;height:380px;border-radius:50%;background:linear-gradient(180deg,var(--coral),var(--orange));display:flex;align-items:center;justify-content:center;font-family:"Poppins",sans-serif;font-weight:600;font-size:46px;color:var(--white)}

/* whitepaper */
.eyebrow{left:677px;top:2920px;font-family:"Poppins",sans-serif;font-weight:500;font-size:17px;color:var(--coral)}
.deal-title{left:677px;top:2944px;font-family:"Poppins",sans-serif;font-weight:600;font-size:45px}
.deal-copy{left:677px;top:3010px;width:440px;font-size:14px;line-height:22.5px;color:var(--muted)}
.deal-cta{left:675px;top:3159px;width:154px;height:42px;background:linear-gradient(90deg,var(--coral),var(--orange));color:var(--white);font-size:13px}

/* faq */
.faq-title{position:absolute;left:0;top:3380px;width:1200px;text-align:center;font-family:"Poppins",sans-serif;font-weight:600;font-size:44px;line-height:53px}
.faq{position:absolute;left:287px;width:626px;background:var(--white);box-shadow:0 4px 18px rgba(0,0,0,.08);padding:0 28px;display:flex;align-items:center;justify-content:space-between;font-family:"Poppins",sans-serif;font-weight:500;font-size:15px}
.faq .plus{font-size:22px;font-weight:600}
.faq.open{display:block;border-left:4px solid var(--orange-deep);padding-top:26px}
.faq.open p{margin-top:10px;font-family:"Raleway",sans-serif;font-weight:500;font-size:13.5px;line-height:22px;color:var(--muted)}

/* sale */
.sale{position:absolute;left:88px;top:3968px;width:1022px;height:130px;border-radius:65px;background:linear-gradient(90deg,var(--orange),var(--coral));z-index:2}
.sale-big{position:absolute;left:67px;top:34px;font-family:"Poppins",sans-serif;font-weight:600;font-size:48px;color:var(--white)}
.sale-text{position:absolute;left:337px;top:33px;font-family:"Poppins",sans-serif;font-weight:500;font-size:26px;line-height:32px;color:var(--white)}
.sale-cta{left:789px;top:37px;width:190px;height:52px;background:var(--white);color:var(--ink);font-size:14px}

/* footer */
.foot-brand{left:155px;top:4276px;display:flex;align-items:center;gap:10px;font-family:"Poppins",sans-serif;font-weight:600;font-size:34px;color:var(--white)}
.foot-text{position:absolute;font-size:13.5px;line-height:22px;color:#e6e6e6}
.foot-head{position:absolute;font-family:"Poppins",sans-serif;font-weight:500;font-size:19px;color:var(--white)}
.foot-socials{position:absolute;left:532px;top:4326px;display:flex;gap:8px}
.foot-socials .social{height:34px;font-size:11px;padding:0 10px}
.contact{position:absolute;left:863px;top:4330px;font-size:13.5px;line-height:23px;color:#e6e6e6}
.contact span{display:inline-block;width:10px;height:10px;background:var(--coral);margin-right:8px;border-radius:2px}
.divider{position:absolute;left:88px;top:4478px;width:1022px;height:1px;background:#444}
.to-top{position:absolute;left:1108px;top:4459px;width:40px;height:40px;border-radius:50%;background:var(--orange-deep);display:flex;align-items:center;justify-content:center}
.copyright{position:absolute;left:0;top:4503px;width:1200px;text-align:center;font-size:13px;color:#e6e6e6}
</style>
</head>
<body>

<!-- HERO BACKGROUND -->
<svg class="abs" style="left:0;top:0" width="1200" height="840" viewBox="0 0 1200 840">
  <defs>
    <linearGradient id="heroGrad" x1="0" y1="0" x2="1" y2="1">
      <stop offset="0" stop-color="#4a12d8"/>
      <stop offset=".45" stop-color="#2b12c8"/>
      <stop offset="1" stop-color="#7a1cf0"/>
    </linearGradient>
    <linearGradient id="edgeGrad" x1="0" y1="0" x2="1" y2="0">
      <stop offset="0" stop-color="#f08f49"/>
      <stop offset="1" stop-color="#e8613c"/>
    </linearGradient>
  </defs>
  <path d="M0 830 C200 838 390 812 580 768 C830 708 1010 560 1200 500 V540 C1010 600 840 740 590 790 C390 828 190 845 0 836 Z" fill="url(#edgeGrad)"/>
  <path d="M0 0 H1200 V500 C1010 560 830 700 580 760 C390 806 190 830 0 820 Z" fill="url(#heroGrad)"/>
  <rect role="img" aria-label="Faint stepped line pattern in violet" x="0" y="0" width="520" height="520" fill="#ffffff" opacity=".04"/>
</svg>

<!-- HEADER -->
<div class="brand"><span class="brand-dot"></span>pagevance</div>
<div class="socials">
  <div class="social">Chirpnet</div>
  <div class="social">Harmlink</div>
  <div class="social">Quillpost</div>
  <div class="social">Wirecast</div>
</div>
<div class="pill-btn header-cta">Join Waitlist</div>

<!-- HERO TEXT -->
<h1 class="hero-title">Free<br><span class="accent">reading</span><br>of books</h1>
<div class="pill-btn hero-cta">Join Waitlist</div>

<!-- HERO MOCKUP -->
<div class="frame" style="left:476px;top:203px;width:160px;height:252px">
  <div class="abs" style="left:10px;top:8px;width:140px;height:18px;background:#2a2a33;border-radius:3px"></div>
  <div class="cover" role="img" aria-label="Book cover in teal and red" style="left:24px;top:68px;width:112px;height:150px;background:linear-gradient(180deg,#49b7b7,#e4566a)"></div>
</div>
<div class="frame" style="left:573px;top:283px;width:537px;height:292px">
  <div class="abs" style="left:0;top:0;width:537px;height:34px;background:#20202a;border-radius:10px 10px 0 0"></div>
  <div class="cover" role="img" aria-label="Book cover with teal sky" style="left:38px;top:70px;width:92px;height:138px;background:linear-gradient(180deg,#bfd8cf,#8b6b54)"></div>
  <div class="cover" role="img" aria-label="Dark book cover with golden grass" style="left:160px;top:70px;width:92px;height:138px;background:linear-gradient(180deg,#1d1d1d,#7a5a2a)"></div>
  <div class="cover" role="img" aria-label="Red book cover with a hand" style="left:283px;top:70px;width:92px;height:138px;background:linear-gradient(180deg,#e63c3c,#c42c34)"></div>
  <div class="bar" style="left:38px;top:222px;width:92px"></div>
  <div class="bar" style="left:160px;top:222px;width:92px"></div>
  <div class="bar" style="left:283px;top:222px;width:92px"></div>
  <div class="bar" style="left:38px;top:240px;width:60px"></div>
  <div class="bar" style="left:160px;top:240px;width:60px"></div>
  <div class="bar" style="left:283px;top:240px;width:60px"></div>
  <div class="bar" style="left:20px;top:266px;width:440px;height:6px"></div>
</div>
<div class="cover" role="img" aria-label="Colourful patterned book cover" style="z-index:2;left:980px;top:255px;width:156px;height:232px;background:linear-gradient(180deg,#5fb3c7,#f0913c 55%,#e54698);box-shadow:0 14px 30px rgba(0,0,0,.3)"></div>
<div class="frame" style="left:518px;top:540px;width:128px;height:192px;border-radius:4px">
  <div class="cover" role="img" aria-label="White book cover with coloured dots" style="left:8px;top:8px;width:112px;height:176px;background:linear-gradient(180deg,#ffffff,#f3f3f3);border:1px solid #eee"></div>
</div>
<div class="frame" style="left:670px;top:642px;width:106px;height:64px;border-radius:6px">
  <div class="bar" style="left:14px;top:22px;width:64px"></div>
  <div class="bar" style="left:14px;top:38px;width:34px;height:6px"></div>
</div>
<div class="frame" style="left:902px;top:563px;width:275px;height:168px;border-radius:4px">
  <div class="abs" style="left:0;top:0;width:275px;height:16px;background:#20202a;border-radius:4px 4px 0 0"></div>
  <div class="cover" role="img" aria-label="Dark book cover with gold lettering" style="left:56px;top:36px;width:58px;height:86px;background:linear-gradient(180deg,#2b2b2b,#8a6a2a)"></div>
  <div class="abs" style="left:220px;top:50px;width:32px;height:8px;background:var(--orange)"></div>
  <div class="abs" style="left:220px;top:64px;width:32px;height:8px;background:var(--orange)"></div>
  <div class="bar" style="left:140px;top:50px;width:60px;height:6px"></div>
  <div class="bar" style="left:140px;top:66px;width:40px;height:6px"></div>
  <div class="bar" style="left:20px;top:142px;width:200px;height:5px"></div>
</div>

<!-- BROWSING BOOKS -->
<h2 class="section-title" style="top:880px">Browsing books</h2>
<div class="book-card" style="left:125px;top:981px">
  <div class="cover" role="img" aria-label="Red book cover" style="background:linear-gradient(180deg,#ef4040,#d8262a)"></div>
  <h3>Heading here</h3><p>Lorem Ipsum has been<br>the industry's</p>
</div>
<div class="book-card" style="left:320px;top:981px">
  <div class="cover" role="img" aria-label="Blue book cover" style="background:linear-gradient(180deg,#5ab6e8,#2f8fcf)"></div>
  <h3>Heading here</h3><p>Lorem Ipsum has been<br>the industry's</p>
</div>
<div class="book-card" style="left:513px;top:981px">
  <div class="cover" role="img" aria-label="Pale green book cover" style="background:linear-gradient(180deg,#c8dcc0,#a9c4a0)"></div>
  <h3>Heading here</h3><p>Lorem Ipsum has been<br>the industry's</p>
</div>
<div class="book-card" style="left:701px;top:981px">
  <div class="cover" role="img" aria-label="Cream book cover" style="background:linear-gradient(180deg,#f8f4ec,#ece6da)"></div>
  <h3>Heading here</h3><p>Lorem Ipsum has been<br>the industry's</p>
</div>
<div class="book-card" style="left:888px;top:981px">
  <div class="cover" role="img" aria-label="Grey and yellow book cover" style="background:linear-gradient(180deg,#5d5d5d,#4a4a4a 80%,#ffffff 80%)"></div>
  <h3>Heading here</h3><p>Lorem Ipsum has been<br>the industry's</p>
</div>

<!-- TEAM -->
<h2 class="section-title" style="top:1340px">Team</h2>
<p class="subtitle" style="top:1399px">We designed it with you in mind and with them by our side.</p>
<div class="member" style="left:141px;top:1449px">
  <div class="photo" role="img" aria-label="Portrait of a team member on teal" style="background:linear-gradient(180deg,#58c4d8,#3aa9c2)"></div>
  <h3>John Smith</h3><p>Documentation</p>
</div>
<div class="member" style="left:368px;top:1449px">
  <div class="photo" role="img" aria-label="Portrait of a team member on grey" style="background:radial-gradient(circle,#6a7076,#3a3f44);outline:2px dotted #f08f49;outline-offset:6px"></div>
  <h3>Alina Jow</h3><p>Documentation</p>
</div>
<div class="member" style="left:592px;top:1449px">
  <div class="photo" role="img" aria-label="Portrait of a team member on blue" style="background:linear-gradient(180deg,#3fb6f0,#1f95d8)"></div>
  <h3>Foan Aloe</h3><p>Documentation</p>
</div>
<div class="member" style="left:817px;top:1449px">
  <div class="photo" role="img" aria-label="Portrait of a team member on orange" style="background:linear-gradient(180deg,#f7b97a,#f2a15c)"></div>
  <h3>Kalen Joh</h3><p>Documentation</p>
</div>

<!-- PEACH WAVE BAND -->
<svg class="abs" style="left:0;top:1720px" width="1200" height="1050" viewBox="0 0 1200 1050">
  <defs>
    <linearGradient id="peachGrad" x1="0" y1="0" x2="0" y2="1">
      <stop offset="0" stop-color="#fdf1e8"/>
      <stop offset=".35" stop-color="#fbdcc8"/>
      <stop offset="1" stop-color="#fde9dc"/>
    </linearGradient>
  </defs>
  <path d="M0 20 C240 80 420 120 640 90 C860 60 1040 10 1200 0 V860 C980 820 780 900 560 960 C360 1020 160 1000 0 990 Z" fill="url(#peachGrad)"/>
  <path d="M0 160 C300 230 520 200 760 170 C960 150 1100 180 1200 200 V840 C1000 800 760 880 540 930 C340 975 140 960 0 950 Z" fill="#fbd8c2" opacity=".55"/>
  <circle cx="111" cy="298" r="46" fill="#ffffff" opacity=".35"/>
</svg>

<!-- ROADMAP -->
<h2 class="section-title" style="top:2057px">Roadmap</h2>
<div class="road-core">pagevance</div>

<div class="road-label left" style="left:38px;top:2267px">Book Launch</div>
<div class="road-label left" style="left:38px;top:2323px">Promotions</div>
<div class="road-label left" style="left:38px;top:2380px">Advertisments</div>
<div class="road-label" style="left:855px;top:2267px">Story synopsis</div>
<div class="road-label" style="left:855px;top:2323px">Author Info</div>
<div class="road-label" style="left:855px;top:2380px">Launch Date</div>

<div class="road-icon" style="left:382px;top:2216px">
  <svg width="36" height="36" viewBox="0 0 36 36" fill="none" stroke="#222" stroke-width="2"><rect x="6" y="6" width="24" height="20" rx="2"/><path d="M4 30 H32 M10 12 H26 M10 18 H22"/></svg>
</div>
<div class="road-icon" style="left:361px;top:2299px">
  <svg width="36" height="36" viewBox="0 0 36 36" fill="none" stroke="#222" stroke-width="2"><path d="M6 15 V21 H11 L24 28 V8 L11 15 Z M11 21 L13 29 H16 M28 14 L32 12 M28 22 L32 24"/></svg>
</div>
<div class="road-icon" style="left:391px;top:2375px">
  <svg width="36" height="36" viewBox="0 0 36 36" fill="none" stroke="#222" stroke-width="2"><rect x="6" y="8" width="24" height="20" rx="2"/><path d="M12 23 L15 13 L18 23 M13 20 H17 M21 13 V23 H23 A4 5 0 0 0 23 13 Z"/></svg>
</div>
<div class="road-icon" style="left:736px;top:2216px">
  <svg width="36" height="36" viewBox="0 0 36 36" fill="none" stroke="#222" stroke-width="2"><path d="M4 28 H32 M6 28 C10 24 14 24 18 28 C22 24 26 24 30 28 M11 22 V14 M18 22 V8 M25 22 V12"/></svg>
</div>
<div class="road-icon" style="left:754px;top:2299px">
  <svg width="36" height="36" viewBox="0 0 36 36" fill="none" stroke="#222" stroke-width="2"><circle cx="18" cy="13" r="6"/><path d="M7 31 C8 23 28 23 29 31"/></svg>
</div>
<div class="road-icon" style="left:724px;top:2375px">
  <svg width="36" height="36" viewBox="0 0 36 36" fill="none" stroke="#222" stroke-width="2"><rect x="6" y="8" width="24" height="22" rx="2"/><path d="M6 14 H30 M12 5 V10 M24 5 V10 M11 19 H13 M17 19 H19 M23 19 H25 M11 24 H13 M17 24 H19 M23 24 H25"/></svg>
</div>

<!-- DECORATIVE NETWORK AREA -->
<div class="abs" role="img" aria-label="Violet hexagon line network decoration" style="left:828px;top:2555px;width:372px;height:300px;background:radial-gradient(ellipse at 60% 50%,rgba(122,28,240,.14),rgba(122,28,240,0) 70%)"></div>

<!-- WHITEPAPER / DEALS -->
<div class="cover" role="img" aria-label="Red book cover with figures" style="left:319px;top:2840px;width:275px;height:425px;background:linear-gradient(180deg,#f03030,#e41e26);box-shadow:0 12px 30px rgba(0,0,0,.2)"></div>
<div class="cover" role="img" aria-label="Navy book cover with golden moon" style="left:132px;top:2825px;width:259px;height:400px;background:radial-gradient(circle at 45% 55%,#6a5a3a,#1f2a44 55%);box-shadow:0 12px 30px rgba(0,0,0,.3)"></div>

<div class="abs eyebrow">WHITEPAPER</div>
<h2 class="abs deal-title">Today Deals In Book</h2>
<p class="abs deal-copy">Lorem Ipsum is simply dummy text of the printing and typesetting industry. Lorem Ipsum has been the industry's standard dummy text ever since the 1500s, when an unknown printer took a galley of type and scrambled it to make a type specimen book. It has survived not only five centuries, but also the leap into electronic typesetting, remaining essentially unchanged.</p>
<div class="pill-btn deal-cta">Read More</div>

<!-- FAQ -->
<h2 class="faq-title">Impress your clients<br>by presenting your branding.</h2>
<div class="faq" style="top:3545px;height:53px">Free Shipping Anywhere<span class="plus">+</span></div>
<div class="faq open" style="top:3612px;height:132px">What level of browser support do you required?
  <p>Lorem Ipsum is simply dummy text of the printing and typesetting industry. Lorem Ipsum has been the industry's standard dummy text ever sinc.</p>
</div>
<div class="faq" style="top:3758px;height:53px">Do you need a fixed width or responsive theme?<span class="plus">+</span></div>
<div class="faq" style="top:3825px;height:53px">&nbsp;&nbsp;Do you need a website or blog based theme?<span class="plus">+</span></div>

<!-- FOOTER BACKGROUND -->
<svg class="abs" style="left:0;top:4060px" width="1200" height="479" viewBox="0 0 1200 479">
  <path d="M0 60 C300 28 700 40 1200 0 V479 H0 Z" fill="#000000"/>
</svg>

<!-- SALE BANNER -->
<div class="sale">
  <div class="sale-big">50% Sale!</div>
  <div class="sale-text">Disc Up to 50% Every Week for<br>selected Item</div>
  <div class="pill-btn sale-cta">Shop Now</div>
</div>

<!-- FOOTER -->
<div class="abs foot-brand"><span class="brand-dot" style="width:52px;height:52px"></span>pagevance</div>
<p class="foot-text" style="left:155px;top:4330px;width:310px">Lorem Ipsum is simply dummy text of the printing and typesetting industry. Lorem Ipsum has been the industry's .</p>

<div class="foot-head" style="left:532px;top:4284px">Connect With Us</div>
<div class="foot-socials">
  <div class="social">Chirpnet</div>
  <div class="social">Harmlink</div>
  <div class="social">Quillpost</div>
  <div class="social">Wirecast</div>
</div>

<div class="foot-head" style="left:863px;top:4284px">Contact Us</div>
<div class="contact">
  <div><span></span>hello@pagevance-mail.io</div>
  <div><span></span>+23 4410 722</div>
  <div><span></span>302 55810 9931</div>
</div>

<div class="divider"></div>
<div class="to-top">
  <svg width="16" height="16" viewBox="0 0 16 16" fill="none" stroke="#fff" stroke-width="2"><path d="M3 10 L8 5 L13 10"/></svg>
</div>
<p class="copyright">©Copyright 2022 | All Rights Reserved</p>

</body>
</html>
```